Flyer Design for an electrical and security company trying to build local customers

I need a flyer design for a new company based in Larkspur Bay, Sydney 2299 called "Harbor Quill Dune Electrical and Security" also "HQD Electrical and Security". We are electrical contractors who are looking for more local work including emergency service calls and any project work including renovations or new constructions in the local area. I would like everyone in the area to know I am new and that I am available 24 hours a day 7 days a week. I would like to see designs that use the logo colours. Would also like the font of the entire design to be "juice bold".

Electrical

• juice bold

Requirements
Must have
• Must use the colours of the original logo and also have the information from the rear of the card. Must also have services buttons like the website picture attached.

```html
<!DOCTYPE html>
<html lang="en">
<head>
<meta charset="utf-8">
<title>Harbor Quill Dune Electrical and Security – Flyers</title>
<link rel="stylesheet" href="https://fonts.googleapis.com/css2?family=Baumans&family=Lexend:wght@400;600;700&display=swap">
<style>
  :root{
    --stage:#000000;
    --paper:#ffffff;
    --cream:#fbf3ea;
    --cream-edge:#f1dfcd;
    --ink:#3c3c3e;
    --charcoal:#4a4a4c;
    --orange:#e08c68;
    --blue:#57b8e8;
    --bolt:#4aa9e0;
    --tile-red:#c9352a;
    --tile-wood:#a4583a;
    --tile-white:#e9e7e3;
    --tile-yellow:#e8d53a;
    --tile-grey:#7c7c80;
    --tile-dark:#2f2f31;
  }
  *{box-sizing:border-box;margin:0;padding:0}
  html,body{width:1200px;height:852px;overflow:hidden;background:var(--stage)}
  body{position:relative;font-family:"Baumans",sans-serif;color:var(--ink)}

  .flyer{position:absolute;top:62px;width:505px;height:711px;background:var(--paper);overflow:hidden}
  .flyer--front{left:90px}
  .flyer--back{left:620px}

  /* front photo grid */
  .tile-grid{position:absolute;left:17px;top:16px;width:472px;height:473px;display:grid;
    grid-template-columns:repeat(5,1fr);grid-template-rows:repeat(5,1fr);gap:4px}
  .tile{display:block}
  .tile--red{background:linear-gradient(135deg,var(--tile-red),#e0573e 60%,var(--tile-wood))}
  .tile--white{background:linear-gradient(135deg,#f7f6f3,var(--tile-white) 60%,#c9c6c0)}
  .tile--wood{background:linear-gradient(135deg,#b8643f,var(--tile-wood))}
  .tile--yellow{background:linear-gradient(135deg,var(--tile-yellow),#c8b030 60%,var(--tile-red))}
  .tile--meter{background:linear-gradient(135deg,var(--tile-dark),var(--tile-grey) 60%,var(--tile-white))}
  .tile--bulb{background:linear-gradient(135deg,var(--tile-white),var(--tile-grey) 60%,var(--tile-wood))}

  .brand-panel{grid-column:2 / 5;grid-row:2 / 5;background:radial-gradient(circle at 50% 45%,#fff 30%,var(--cream) 70%,var(--cream-edge));
    display:flex;flex-direction:column;align-items:center;justify-content:center;text-align:center}
  .brand-name{font-family:"Baumans",sans-serif;color:var(--ink);font-size:50px;line-height:0.95;letter-spacing:-0.5px}
  .ribbon{display:inline-block;background:var(--charcoal);color:#fff;font-family:"Baumans",sans-serif;
    clip-path:polygon(0 0,100% 0,96% 50%,100% 100%,0 100%,4% 50%)}
  .brand-panel .ribbon{margin-top:22px;font-size:17px;padding:3px 22px;letter-spacing:0.5px}
  .sectors{margin-top:9px;font-family:"Lexend",sans-serif;font-size:11.5px;color:var(--ink)}

  /* shared footer */
  .tagline-band{position:absolute;left:0;top:503px;width:100%;height:49px;background:var(--orange);
    display:flex;align-items:center;justify-content:center;font-size:27px;color:var(--ink);letter-spacing:0.3px}
  .contact-band{position:absolute;left:0;top:552px;width:100%;height:159px;background:var(--blue);text-align:center;color:var(--ink)}
  .call-label{margin-top:13px;font-family:"Lexend",sans-serif;font-weight:600;font-size:15.5px}
  .phone{font-family:"Lexend",sans-serif;font-weight:700;font-size:42px;line-height:1.1;letter-spacing:0.5px}
  .company{margin-top:4px;font-family:"Lexend",sans-serif;font-weight:600;font-size:17.5px}
  .address,.links{font-family:"Lexend",sans-serif;font-size:12.5px;display:flex;justify-content:center;align-items:center;gap:5px}
  .address{margin-top:4px}
  .links{gap:6px}
  .links svg,.address svg{flex:none}

  /* back */
  .info-panel{position:absolute;left:17px;top:17px;width:471px;height:473px;
    background:radial-gradient(ellipse at 50% 50%,#fff 45%,var(--cream) 80%,var(--cream-edge))}
  .back-brand{position:absolute;left:30px;top:36px;width:200px}
  .back-brand .brand-name{font-size:44px;text-align:left}
  .back-brand .ribbon{margin-top:14px;font-size:14px;padding:2px 16px}
  .job-photo{position:absolute;left:256px;top:16px;width:214px;height:161px;
    background:linear-gradient(135deg,#d9dde0,#9aa6b0 45%,#5d7a92 70%,#c79a80)}
  .intro{position:absolute;left:0;top:195px;width:100%;text-align:center;font-size:15.5px;line-height:19px;color:var(--ink)}
  .cover-ribbon{position:absolute;left:50%;top:285px;transform:translateX(-50%);background:var(--orange);color:var(--ink);
    font-family:"Lexend",sans-serif;font-weight:600;font-size:15px;padding:3px 44px;
    clip-path:polygon(0 0,100% 0,94% 50%,100% 100%,0 100%,6% 50%)}
  .service-list{position:absolute;top:320px;list-style:none;font-size:15.5px;line-height:20.1px;color:var(--ink)}
  .service-list--left{left:68px}
  .service-list--right{left:259px}
  .service-list li{display:flex;align-items:center;gap:5px;white-space:nowrap}
</style>
</head>
<body>
<svg width="0" height="0" style="position:absolute">
  <defs>
    <symbol id="bolt" viewBox="0 0 10 16"><path d="M6 0 L1 9 H5 L3.5 16 L9 6 H5 Z" fill="#4aa9e0"/></symbol>
    <symbol id="pin" viewBox="0 0 12 16"><path d="M6 0a5.5 5.5 0 0 0-5.5 5.5C.5 10 6 16 6 16s5.5-6 5.5-10.5A5.5 5.5 0 0 0 6 0z" fill="#e08c68"/><circle cx="6" cy="5.5" r="2" fill="#57b8e8"/></symbol>
    <symbol id="globe" viewBox="0 0 14 14"><circle cx="7" cy="7" r="6" fill="none" stroke="#e08c68" stroke-width="1.6"/><path d="M1 7h12M7 1c-3 3-3 9 0 12M7 1c3 3 3 9 0 12" fill="none" stroke="#e08c68" stroke-width="1.2"/></symbol>
    <symbol id="social" viewBox="0 0 14 14"><rect x="1" y="1" width="12" height="12" rx="2" fill="#e08c68"/></symbol>
  </defs>
</svg>

<!-- front -->
<section class="flyer flyer--front">
  <div class="tile-grid">
    <span class="tile tile--red" role="img" aria-label="Photo of red-handled wire cutters"></span>
    <span class="tile tile--white" role="img" aria-label="Photo of a spiral energy-saving bulb"></span>
    <span class="tile tile--white" role="img" aria-label="Photo of a white power outlet with screws"></span>
    <span class="tile tile--meter" role="img" aria-label="Photo of multimeter sockets"></span>
    <span class="tile tile--red" role="img" aria-label="Photo of red pliers"></span>

    <span class="tile tile--bulb" role="img" aria-label="Photo of a light bulb base"></span>
    <div class="brand-panel">
      <div class="brand-name">Harbor<br>Quill<br>Dune</div>
      <div class="ribbon">Electrical and security</div>
      <div class="sectors">Residential • Commercial• Industrial</div>
    </div>
    <span class="tile tile--wood" role="img" aria-label="Photo of a red test probe"></span>

    <span class="tile tile--yellow" role="img" aria-label="Photo of yellow cable coil"></span>
    <span class="tile tile--bulb" role="img" aria-label="Photo of a bulb screw base"></span>

    <span class="tile tile--meter" role="img" aria-label="Photo of a multimeter with leads"></span>
    <span class="tile tile--red" role="img" aria-label="Photo of red crimping tool"></span>

    <span class="tile tile--red" role="img" aria-label="Photo of electrical tape"></span>
    <span class="tile tile--meter" role="img" aria-label="Photo of a multimeter dial"></span>
    <span class="tile tile--bulb" role="img" aria-label="Photo of light bulbs"></span>
    <span class="tile tile--meter" role="img" aria-label="Photo of test leads"></span>
    <span class="tile tile--white" role="img" aria-label="Photo of a spiral bulb close-up"></span>
  </div>

  <div class="tagline-band">24 hour Emergency Serivce</div>
  <div class="contact-band">
    <p class="call-label">Call us Today</p>
    <p class="phone">1300 555 019</p>
    <p class="company">Harbor Quill Dune Electrical and Security</p>
    <p class="address"><svg width="9" height="12"><use href="#pin"/></svg>Larkspur Bay, Sydney 2299</p>
    <p class="links"><svg width="12" height="12"><use href="#globe"/></svg>www.harborquilldune.com.au <svg width="12" height="12"><use href="#social"/></svg>harborquilldune</p>
  </div>
</section>

<!-- back -->
<section class="flyer flyer--back">
  <div class="info-panel">
    <div class="back-brand">
      <div class="brand-name">Harbor<br>Quill<br>Dune</div>
      <div class="ribbon">Electrical and security</div>
    </div>
    <div class="job-photo" role="img" aria-label="Photo of an electrician drilling a fitting into a wall"></div>

    <p class="intro">We do All House Rennovations, Construction, Commercial<br>24 Hours Emergency Service, New Installations, Repairs<br>Maintenance, Home Theater and So on...</p>

    <div class="cover-ribbon">WE COVER</div>

    <ul class="service-list service-list--left">
      <li><svg width="9" height="14"><use href="#bolt"/></svg>New Installations</li>
      <li><svg width="9" height="14"><use href="#bolt"/></svg>Repaires</li>
      <li><svg width="9" height="14"><use href="#bolt"/></svg>Maintenance</li>
      <li><svg width="9" height="14"><use href="#bolt"/></svg>REnovations/Extensions</li>
      <li><svg width="9" height="14"><use href="#bolt"/></svg>RE-wiring</li>
      <li><svg width="9" height="14"><use href="#bolt"/></svg>home theater</li>
      <li><svg width="9" height="14"><use href="#bolt"/></svg>surronds sound</li>
      <li><svg width="9" height="14"><use href="#bolt"/></svg>Wall Tv's</li>
    </ul>
    <ul class="service-list service-list--right">
      <li><svg width="9" height="14"><use href="#bolt"/></svg>Electric Hot Water</li>
      <li><svg width="9" height="14"><use href="#bolt"/></svg>Stoves, Cooktops</li>
      <li><svg width="9" height="14"><use href="#bolt"/></svg>Lighting</li>
      <li><svg width="9" height="14"><use href="#bolt"/></svg>Celling Fans</li>
      <li><svg width="9" height="14"><use href="#bolt"/></svg>Testing and Tagging</li>
      <li><svg width="9" height="14"><use href="#bolt"/></svg>Data</li>
      <li><svg width="9" height="14"><use href="#bolt"/></svg>Telephone</li>
      <li><svg width="9" height="14"><use href="#bolt"/></svg>Security Systems</li>
    </ul>
  </div>

  <div class="tagline-band">Available 24 hours a day 7 days a week</div>
  <div class="contact-band">
    <p class="call-label">Call us Today</p>
    <p class="phone">1300 555 019</p>
    <p class="company">Harbor Quill Dune Electrical and Security</p>
    <p class="address"><svg width="9" height="12"><use href="#pin"/></svg>Larkspur Bay, Sydney 2299</p>
    <p class="links"><svg width="12" height="12"><use href="#globe"/></svg>www.harborquilldune.com.au <svg width="12" height="12"><use href="#social"/></svg>harborquilldune</p>
  </div>
</section>
</body>
</html>
```